Crooked Thunder

I would like a website that does e-commerce and able to take payments for merchandise and orders.
Updates

Target Market(s)

Skate, BMX, surf, drink, adventure, motorcycle, rock n roll, bars, hot rods, tattoos, rebels

Industry/Entity Type

Brand market

Coding

Coded - Design and coding required

Number of Pages Required

1 page

Font styles to use
Serif

Requirements
Must have
• E-commerce
Nice to have
• Pictures of merch on people... Ex. People wearing our hats

```html
<!DOCTYPE html>
<html lang="en">
<head>
<meta charset="utf-8">
<title>Crooked Thunder</title>
<link rel="stylesheet" href="https://fonts.googleapis.com/css2?family=Josefin+Sans:ital,wght@0,300;0,400;0,600;0,700;1,300;1,400&display=swap">
<style>
:root{
  --teal:#22b5bd;
  --teal-soft:#b7e3e6;
  --teal-pale:#d3eef0;
  --orange:#f37021;
  --orange-pale:#fde0cc;
  --ink:#1d1d1f;
  --grey:#8a8a8a;
  --white:#ffffff;
}
*{box-sizing:border-box;margin:0;padding:0}
html,body{width:1200px;height:4451px;overflow:hidden;background:var(--white)}
body{font-family:"Josefin Sans",sans-serif;color:var(--ink)}
.page{position:relative;width:1200px;height:4451px;overflow:hidden}
.abs{position:absolute}
.btn{position:absolute;display:flex;align-items:center;justify-content:center;background:var(--orange);color:var(--white);border-radius:40px;font-weight:600;font-size:15px;letter-spacing:.5px;text-transform:uppercase;text-decoration:none}
.photo{position:absolute;overflow:hidden}

/* header */
.site-header{position:absolute;left:0;top:0;width:1200px;height:86px;background:var(--white)}
.brand{position:absolute;left:145px;top:10px;width:160px;height:160px;border-radius:50%;background:var(--white);border:3px solid var(--ink);display:flex;align-items:center;justify-content:center;text-align:center;font-weight:700;font-size:21px;line-height:1.1;color:var(--ink);z-index:3;text-transform:uppercase}
.nav-link{position:absolute;top:36px;font-size:16px;color:var(--ink);text-decoration:none;white-space:nowrap}
.icon-btn{position:absolute;top:30px;width:30px;height:30px;border-radius:50%}

/* hero */
.hero-title{position:absolute;left:140px;top:210px;font-size:62px;line-height:1.12;font-weight:700;color:var(--white);letter-spacing:2px}
.hero-sub{position:absolute;left:143px;top:360px;font-size:25px;font-weight:600;color:var(--white)}

/* products */
.section-title{position:absolute;left:0;width:1200px;text-align:center;font-size:41px;font-weight:700;letter-spacing:1px}
.product{position:absolute;width:280px;text-align:center}
.product .ring{width:276px;height:276px;margin:0 auto;border-radius:50%;border:3px solid var(--ink);display:flex;align-items:center;justify-content:center;background:var(--white)}
.product .ring.dashed{border:4px dotted var(--ink)}
.product .img{width:248px;height:248px;border-radius:50%}
.product .name{margin-top:27px;font-size:18px;font-weight:600;letter-spacing:1px}
.product .price{margin-top:8px;font-size:16px;font-weight:700;color:var(--orange)}

/* about */
.about-title{position:absolute;left:145px;top:1968px;font-size:41px;font-weight:700}
.about-text{position:absolute;left:145px;top:2032px;width:445px;font-size:15px;line-height:25px;font-weight:300;text-align:justify}

/* blogs */
.card{position:absolute;top:2690px;width:436px;height:470px;background:var(--white);box-shadow:0 1px 6px rgba(0,0,0,.15)}
.card .photo{left:0;top:0;width:436px;height:268px}
.card .date{position:absolute;left:34px;top:208px;width:46px;height:42px;border:2px solid var(--white);color:var(--white);font-size:11px;font-weight:700;text-align:center;line-height:15px;padding-top:5px}
.card h3{position:absolute;left:23px;top:296px;width:395px;font-size:18px;font-weight:700;line-height:22px;letter-spacing:.3px}
.card p{position:absolute;left:23px;width:380px;font-size:12px;line-height:20px;font-weight:300;color:#555}
.card .more{position:absolute;left:23px;top:434px;font-size:13px;color:var(--orange);text-decoration:underline;font-weight:600}

/* reviews */
.reviews-title{position:absolute;left:0;top:3480px;width:1200px;text-align:center;font-size:43px;font-weight:700;color:var(--white);letter-spacing:1px}
.review-text{position:absolute;left:190px;top:3625px;width:820px;text-align:center;font-size:20px;line-height:31px;font-style:italic;font-weight:300;color:var(--white)}
.review-name{position:absolute;left:0;top:3735px;width:1200px;text-align:center;font-size:20px;font-weight:600;color:var(--white)}
.arrow{position:absolute;top:3828px;width:44px;height:44px;border:2px solid var(--white);border-radius:50%}

/* mailing + footer */
.mail-title{position:absolute;left:145px;top:4120px;font-size:28px;font-weight:700}
.mail-input{position:absolute;left:536px;top:4118px;width:384px;height:38px;border:1px solid #bbb;font-size:13px;padding:12px 20px;color:#333}
.footer-col{position:absolute;top:4210px}
.footer-col h4{font-size:16px;font-weight:600;margin-bottom:14px}
.footer-col li{list-style:none;font-size:13px;color:var(--grey);line-height:23px;font-weight:300}
.social{display:flex;gap:8px;margin-top:6px}
.social span{width:28px;height:28px;border-radius:50%;color:var(--white);font-size:13px;font-weight:700;display:flex;align-items:center;justify-content:center}
.card-pay{display:inline-flex;align-items:center;justify-content:center;width:34px;height:20px;border-radius:3px;font-size:8px;font-weight:700;color:var(--white);margin-right:4px}
.copy{position:absolute;right:145px;top:4408px;font-size:13px;color:#555;font-weight:300}
</style>
</head>
<body>
<div class="page">

  <!-- hero background -->
  <svg class="abs" style="left:0;top:0" width="1200" height="720" viewBox="0 0 1200 720">
    <path d="M0 86H1200V490C1020 620 820 690 600 690C380 690 160 610 0 470Z" fill="var(--teal)"/>
    <path d="M0 500C160 630 380 700 600 700C820 700 1020 630 1200 500" fill="none" stroke="var(--teal-soft)" stroke-width="2"/>
    <circle cx="584" cy="643" r="3" fill="var(--white)"/><circle cx="600" cy="643" r="3" fill="var(--orange)"/><circle cx="616" cy="643" r="3" fill="var(--white)"/>
  </svg>
  <div class="photo" style="left:575px;top:86px;width:440px;height:570px;background:linear-gradient(180deg,#3fbcc2 0%,#7a6e63 40%,#3a8d8f 75%,#2aa9b0 100%);border-radius:0 0 200px 200px;opacity:.85" role="img" aria-label="Young skater in cap, sunglasses and plaid shirt crouching on a skateboard"></div>

  <header class="site-header">
    <div class="brand">Crooked<br>Thunder</div>
    <nav>
      <a class="nav-link" style="left:465px">HOME</a>
      <a class="nav-link" style="left:552px">ABOUT</a>
      <a class="nav-link" style="left:644px">PRODUCTS</a>
      <a class="nav-link" style="left:767px">NEWS</a>
      <a class="nav-link" style="left:852px">CONTACT US</a>
    </nav>
    <svg class="abs" style="left:455px;top:18px" width="70" height="20"><path d="M5 18Q35-4 65 18" fill="none" stroke="var(--ink)" stroke-width="2"/></svg>
    <svg class="icon-btn" style="left:983px" viewBox="0 0 30 30"><circle cx="15" cy="15" r="15" fill="var(--orange)"/><circle cx="13" cy="13" r="5" fill="none" stroke="#fff" stroke-width="2"/><path d="M17 17l5 5" stroke="#fff" stroke-width="2.5"/></svg>
    <svg class="icon-btn" style="left:1023px" viewBox="0 0 30 30"><circle cx="15" cy="15" r="15" fill="var(--ink)"/><path d="M8 9h3l2 8h8l2-6H12" fill="none" stroke="#fff" stroke-width="2"/><circle cx="14" cy="21" r="1.5" fill="#fff"/><circle cx="20" cy="21" r="1.5" fill="#fff"/></svg>
  </header>

  <h1 class="hero-title">CROOKED<br>THUNDER</h1>
  <p class="hero-sub">Sed ut perspiciatis undeatus</p>
  <a class="btn" style="left:143px;top:424px;width:200px;height:56px">Shop Products</a>

  <!-- featured products -->
  <h2 class="section-title" style="top:795px">FEATURED PRODUCTS</h2>
  <div class="product" style="left:149px;top:894px"><div class="ring"><div class="img" style="background:linear-gradient(135deg,#7f8e97,#c9a79a)" role="img" aria-label="Wrist wearing a white branded band"></div></div><div class="name">ACCUSANTIUM</div><div class="price">$56.90</div></div>
  <div class="product" style="left:460px;top:894px"><div class="ring dashed"><div class="img" style="background:linear-gradient(160deg,#9aa5ad,#2c2b2d 60%,#b58a6a)" role="img" aria-label="Man adjusting a black branded cap"></div></div><div class="name">DOLOREMQUE</div><div class="price">$56.90</div></div>
  <div class="product" style="left:771px;top:894px"><div class="ring"><div class="img" style="background:linear-gradient(180deg,#8bb4c7,#4d7e90 55%,#d8c27a)" role="img" aria-label="Surfer in black shirt carrying a yellow board by the sea"></div></div><div class="name">LAUDANTIUM</div><div class="price">$56.90</div></div>

  <div class="product" style="left:149px;top:1276px"><div class="ring"><div class="img" style="background:linear-gradient(150deg,#1f8f7f,#3fae9c 50%,#e98a3a)" role="img" aria-label="Young surfer riding a green wave"></div></div><div class="name">ACCUSANTIUM</div><div class="price">$56.90</div></div>
  <div class="product" style="left:460px;top:1276px"><div class="ring"><div class="img" style="background:linear-gradient(180deg,#e3cda5,#1e1e20 65%)" role="img" aria-label="Man in black cap and branded black t-shirt"></div></div><div class="name">DOLOREMQUE</div><div class="price">$56.90</div></div>
  <div class="product" style="left:771px;top:1276px"><div class="ring"><div class="img" style="background:linear-gradient(160deg,#f58aa0,#f3c9c4 60%,#ef6f8a)" role="img" aria-label="Legs in pink roller skates on a pink background"></div></div><div class="name">LAUDANTIUM</div><div class="price">$56.90</div></div>

  <a class="btn" style="left:475px;top:1675px;width:250px;height:59px">View All Products</a>

  <!-- about -->
  <svg class="abs" style="left:0;top:1790px" width="1200" height="730" viewBox="0 0 1200 730">
    <path d="M0 170C200 30 500 10 760 60C960 95 1120 60 1200 140V560C1080 690 760 720 420 640C220 600 80 620 0 560Z" fill="var(--teal-pale)"/>
    <path d="M0 200C220 90 480 100 700 170C900 230 1100 190 1200 180V500C1050 650 820 700 580 650C360 610 150 560 0 460Z" fill="var(--teal-soft)" opacity=".8"/>
    <circle cx="851" cy="368" r="204" fill="none" stroke="var(--ink)" stroke-width="4" stroke-dasharray="14 8"/>
  </svg>
  <div class="photo" style="left:736px;top:2005px;width:230px;height:300px;border-radius:50% 50% 40% 40%;background:radial-gradient(ellipse at 50% 45%,#7a6a5c 0%,#5a6d73 35%,rgba(183,227,230,0) 70%)" role="img" aria-label="Young man with backpack walking and carrying a longboard"></div>
  <h2 class="about-title">ABOUT US</h2>
  <p class="about-text">Sed ut perspiciatis unde omnis iste natus error sit voluptatem accusantium doloremque laudantium, totam rem aperiam, eaque ipsa quae ab illo inventore veritatis et quasi architecto beatae vitae dicta sunt explicabo. Nemo enim ipsam voluptatem quia voluptas sit aspernatur aut odit aut fugit, sed quia consequuntur magni dolores eos qui ratione voluptatem sequi nesciunt. Neque porro quisquam est, qui dolorem ipsum quia dolor sit amet, consectetur</p>
  <a class="btn" style="left:145px;top:2265px;width:163px;height:60px">Read More</a>

  <!-- blogs -->
  <h2 class="section-title" style="top:2597px">LATEST BLOGS</h2>
  <article class="card" style="left:143px">
    <div class="photo" style="background:linear-gradient(160deg,#1f3a2f,#3d5a3a 45%,#c9a07a 70%,#2e6f9a)" role="img" aria-label="Smiling woman in helmet riding a zipline through the forest"></div>
    <div class="date">APRI<br>2024</div>
    <h3>Sed ut perspiciatis unde omnis iste natus</h3>
    <p style="top:334px">Nemo enim ipsam voluptatem quia voluptas sit aspernatur aut odit aut fugit, sed quia consequuntur magni dolores eos qui ratione voluptatem sequi nesciunt quia non numquam eius modi tempora incidunt ut labore et.</p>
    <a class="more">LEARN MORE</a>
  </article>
  <article class="card" style="left:621px;border:1px solid #9dcfd2">
    <div class="photo" style="background:linear-gradient(180deg,#4e86c4,#90b6d8 40%,#c8702c 60%,#5d6a73)" role="img" aria-label="Woman in helmet and orange vest riding a motorcycle"></div>
    <div class="date" style="background:var(--orange)">APRI<br>2024</div>
    <h3>Ut enim ad minima venia quis nostrum exercitationem ullam corporis</h3>
    <p style="top:357px">Nemo enim ipsam voluptatem quia voluptas sit aspernatur aut odit aut fugit, sed quia consequuntur magni dolores eos qui ratione voluptatem sequi nesciuntsed quia non numquam</p>
    <a class="more">LEARN MORE</a>
  </article>
  <a class="btn" style="left:520px;top:3206px;width:161px;height:59px">Load More</a>

  <!-- reviews -->
  <svg class="abs" style="left:0;top:3300px" width="1200" height="760" viewBox="0 0 1200 760">
    <path d="M0 170C220 80 500 70 700 50C900 30 1120 60 1200 140V660C1000 740 700 760 420 740C200 725 60 690 0 650Z" fill="var(--orange-pale)"/>
    <path d="M0 190C180 110 420 40 640 70C820 95 1000 120 1200 200V560C1020 690 760 730 520 700C300 680 120 620 0 560Z" fill="var(--orange)"/>
  </svg>
  <div class="photo" style="left:470px;top:3520px;width:280px;height:300px;border-radius:50%;background:radial-gradient(circle,rgba(200,80,20,.5),rgba(243,112,33,0) 70%)" role="img" aria-label="Faint image of a skater mid-trick behind the review"></div>
  <h2 class="reviews-title">CUSTOMER REVIEWS</h2>
  <svg class="abs" style="left:575px;top:3565px" width="50" height="40" viewBox="0 0 50 40"><path d="M4 38V22Q4 6 20 2V10Q12 12 12 20H20V38Z M28 38V22Q28 6 44 2V10Q36 12 36 20H44V38Z" fill="#fff"/></svg>
  <p class="review-text">"Nemo enim ipsam voluptatem quia voluptas sit aspernatur aut odit aut fugit, sed quia consequuntur magni dolores eos qui ratione voluptatem sequi nesciuntsed quia non numquam eius modi tempora incidunt ut labore et.</p>
  <p class="review-name">-John Doe,Customer</p>
  <svg class="abs" style="left:549px;top:3778px" width="102" height="20" viewBox="0 0 102 20"><g fill="#fff"><path id="st" d="M10 1l2.6 5.6 6 .7-4.4 4.1 1.2 6L10 14.4 4.6 17.4l1.2-6L1.4 7.3l6-.7z"/><use href="#st" x="20"/><use href="#st" x="40"/><use href="#st" x="60"/><use href="#st" x="80"/></g></svg>
  <svg class="arrow" style="left:549px" viewBox="0 0 44 44"><path d="M25 14l-8 8 8 8" fill="none" stroke="#fff" stroke-width="2"/></svg>
  <svg class="arrow" style="left:606px" viewBox="0 0 44 44"><path d="M19 14l8 8-8 8" fill="none" stroke="#fff" stroke-width="2"/></svg>

  <!-- mailing -->
  <h2 class="mail-title">JOIN OUR MAILING LIST</h2>
  <div class="mail-input">Enter Email</div>
  <a class="btn" style="left:928px;top:4118px;width:128px;height:38px;font-size:14px">Sign Up</a>

  <!-- footer -->
  <div class="footer-col" style="left:145px">
    <h4>Contact us</h4>
    <ul>
      <li style="display:flex;gap:10px"><svg width="16" height="16" viewBox="0 0 16 16"><path d="M2 8L8 2l6 6v6H10v-4H6v4H2z" fill="var(--orange)"/></svg><span>134,Sed ut perspiciatis unde<br>omnis iste natus erro.</span></li>
      <li style="display:flex;gap:10px;margin-top:4px"><svg width="16" height="16" viewBox="0 0 16 16"><path d="M3 1l3 1 1 4-2 1q1 3 4 4l1-2 4 1 1 3-2 2Q4 14 1 3z" fill="var(--orange)"/></svg><span>Call us : +1 555 014 2290</span></li>
    </ul>
  </div>
  <div class="footer-col" style="left:410px">
    <h4>Accounts &amp; Orders</h4>
    <ul><li>Gift Certificates</li><li>Wishlist</li><li>Login or Sign up</li><li>Shipping &amp; Returns</li><li>Sitemap</li></ul>
  </div>
  <div class="footer-col" style="left:652px">
    <h4>Quick Links</h4>
    <ul><li>Why Choose us</li><li>Shipping &amp; returns</li><li>Contact us</li><li>Blog</li></ul>
  </div>
  <div class="footer-col" style="left:858px">
    <h4>Recent Blog Posts</h4>
    <ul><li>Your first blog Post!</li></ul>
    <h4 style="margin-top:14px;margin-bottom:8px">Connect with us</h4>
    <div class="social">
      <span style="background:#2c3e8f" aria-label="Kinnect">K</span>
      <span style="background:#c4161c" aria-label="Pinwall">P</span>
      <span style="background:#d9302a" aria-label="Vidstream">V</span>
      <span style="background:#b59a6a" aria-label="Snapgrid">S</span>
    </div>
  </div>
  <svg class="abs" style="left:1110px;top:4339px" width="46" height="46" viewBox="0 0 46 46"><circle cx="23" cy="23" r="21" fill="#fff" stroke="var(--ink)" stroke-width="2.5"/><circle cx="23" cy="23" r="15" fill="none" stroke="var(--ink)" stroke-width="2"/><path d="M23 32V15M16 21l7-7 7 7" fill="none" stroke="var(--ink)" stroke-width="3"/></svg>

  <div class="abs" style="left:145px;top:4404px">
    <span class="card-pay" style="background:#e46b1c">Ringpay</span><span class="card-pay" style="background:#23408e">Norpay</span><span class="card-pay" style="background:#2f7cc1">Bluecard</span><span class="card-pay" style="background:#444">Tollcard</span>
  </div>
  <p class="copy">© copyright 2024 Crooked Thunder. All Rights Reserved &nbsp;|&nbsp; Privacy policy</p>
</div>
</body>
</html>
```